Mediation Website Design Upgrade

Project Details: https://files.brellowin.net/sheet/v/8kPw3xTzLmQa7NbYr2HdVcEuFj_9Gs-41kh5XoWe/view?mode=public

Number of Pages Required

2 page

Font styles to use
Sans Serif

```html
<!DOCTYPE html>
<html lang="en">
<head>
<meta charset="utf-8">
<title>Harborline Mediation Group</title>
<link rel="stylesheet" href="https://fonts.googleapis.com/css2?family=Montserrat:wght@500;600&family=Nunito:wght@400;600;700&display=swap">
<style>
:root{
  --ink:#1f2a2a;
  --text:#4a4f52;
  --teal:#4f807d;
  --teal-deep:#35625f;
  --green:#6b9b2c;
  --slate:#5f6672;
  --white:#ffffff;
  --line:#e6e9e8;
}
*{box-sizing:border-box;margin:0;padding:0}
html,body{width:1200px;height:3128px;overflow:hidden;background:var(--white)}
body{position:relative;font-family:'Nunito',sans-serif;color:var(--text)}
.abs{position:absolute}
h1,h2,h3{font-family:'Montserrat',sans-serif;font-weight:500;text-transform:uppercase}

/* header */
.site-header{left:0;top:0;width:1200px;height:97px;background:var(--white)}
.brand{left:90px;top:32px;display:flex;align-items:center;gap:12px}
.brand-dot{width:34px;height:34px;border-radius:50%;background:var(--teal)}
.brand-name{font-size:18px;font-weight:700;color:var(--ink);white-space:nowrap}
.main-nav{left:378px;top:40px;display:flex;gap:30px;font-size:17px;color:var(--ink);white-space:nowrap}
.main-nav .active{font-weight:700}

/* hero */
.hero-photo{left:0;top:97px;width:1200px;height:586px;background:linear-gradient(90deg,#5f6672 0%,#5f6672 27%,#7a7772 40%,#b8b0a6 60%,#8b8886 80%,#6f6a66 100%)}
.hero-title{left:113px;top:283px;font-size:52px;line-height:48px;color:var(--white)}
.hero-sub{left:116px;top:392px;width:440px;font-size:19px;line-height:31px;color:var(--white)}
.arrow{top:338px}
.arrow-left{left:34px}
.arrow-right{left:1142px}

.service-cards{left:113px;top:607px;width:974px;height:282px;display:flex}
.card{flex:1;display:flex;flex-direction:column;align-items:center;padding-top:36px;color:var(--white);text-align:center}
.card-commercial,.card-nonprofit{background:linear-gradient(135deg,rgba(79,128,125,.92),rgba(79,128,125,.96))}
.card-family{background:linear-gradient(135deg,#6e9a2f,#6a9a26)}
.card-art{width:80px;height:72px;border-radius:8px;background:rgba(255,255,255,.2)}
.card h3{font-size:24px;line-height:29px;margin-top:14px}
.card p{font-size:11.5px;line-height:19px;margin-top:10px;width:220px;opacity:.9}

/* intro */
.intro-photo{left:113px;top:979px;width:446px;height:395px;background:linear-gradient(135deg,#9a8a76 0%,#b8a690 45%,#3a4f8c 70%,#6f6457 100%)}
.section-title{font-size:32px;line-height:44px;color:var(--ink)}
.rule{width:48px;height:4px;background:var(--teal)}
.intro-title{left:599px;top:996px}
.intro-rule{left:599px;top:1088px}
.intro-text{left:599px;top:1124px;width:530px;font-size:14.5px;line-height:23px}
.intro-text p+p{margin-top:13px}

/* peace band */
.peace-band{left:0;top:1464px;width:1200px;height:511px;background:linear-gradient(120deg,#3e3a2c 0%,#5a5440 35%,#6a6450 60%,#3a3a2e 100%)}
.peace-shade{left:0;top:1464px;width:1200px;height:511px;background:rgba(30,30,25,.35)}
.peace-title{left:0;top:1540px;width:1200px;text-align:center;font-size:32px;color:var(--white)}
.peace-rule{left:578px;top:1583px;width:48px;height:3px;background:var(--white)}
.peace-text{left:175px;top:1605px;width:850px;text-align:center;color:var(--white);font-size:16.5px;line-height:23.5px}
.peace-text p+p{margin-top:13px}
.btn-solid{left:457px;top:1832px;width:278px;height:57px;background:var(--green);color:var(--white);font-size:16px;font-weight:600;display:flex;align-items:center;justify-content:center}

/* services */
.services-title{left:95px;top:2088px;line-height:38px}
.services-rule{left:95px;top:2170px}
.services-text{left:97px;top:2196px;width:475px;font-size:14.5px;line-height:24.5px}
.services-photo{left:599px;top:1975px;width:601px;height:492px;background:linear-gradient(135deg,#d9d6cf 0%,#8a8c93 35%,#3f5f95 65%,#c9c7c2 100%)}

/* consultation */
.consult-band{left:0;top:2467px;width:1200px;height:424px;background:linear-gradient(90deg,#4e7f6f 0%,#5d8d4c 50%,#6a9a2e 100%)}
.consult-title{left:0;top:2570px;width:1170px;text-align:center;font-size:30px;color:var(--white)}
.consult-rule{left:563px;top:2614px;width:48px;height:3px;background:var(--white)}
.consult-text{left:200px;top:2635px;width:770px;text-align:center;font-size:19px;line-height:31px;color:var(--white)}
.btn-outline{left:432px;top:2718px;width:311px;height:54px;border:2px solid var(--white);color:var(--white);font-size:15px;display:flex;align-items:center;justify-content:center}

/* footer */
.footer-brand{left:0;top:2925px;width:1200px;display:flex;justify-content:center;align-items:center;gap:10px;font-size:16px;font-weight:700;color:var(--ink)}
.footer-dot{width:22px;height:22px;border-radius:50%;background:var(--teal)}
.footer-nav{left:0;top:2990px;width:1200px;display:flex;justify-content:center;gap:31px;font-size:17px;color:var(--ink)}
.copyright{left:0;top:3025px;width:1200px;text-align:center;font-size:13px;color:var(--ink)}
.social{left:0;top:3057px;width:1200px;display:flex;justify-content:center;gap:5px}
.social span{width:40px;height:40px;border-radius:50%;border:2px solid var(--green)}
</style>
</head>
<body>

<header class="abs site-header">
  <div class="abs brand"><span class="brand-dot"></span><span class="brand-name">Harborline Mediation Group</span></div>
  <nav class="abs main-nav">
    <span class="active">Home</span><span>Mediation Services</span><span>Conflict Consulting</span><span>Negotiation</span><span>About Us</span><span>Blog</span><span>Contact</span>
  </nav>
</header>

<div class="abs hero-photo" role="img" aria-label="A couple sitting apart on a sofa during a tense conversation at home"></div>
<h1 class="abs hero-title">Family<br>Mediation</h1>
<p class="abs hero-sub">Praesent sit amet est In dictum dolor eu dictum porttitor enim felis viverra mi eget</p>
<svg class="abs arrow arrow-left" width="24" height="42" viewBox="0 0 24 42"><path d="M20 4 L5 21 L20 38" fill="none" stroke="#fff" stroke-width="5"/></svg>
<svg class="abs arrow arrow-right" width="24" height="42" viewBox="0 0 24 42"><path d="M4 4 L19 21 L4 38" fill="none" stroke="#fff" stroke-width="5"/></svg>

<section class="abs service-cards">
  <div class="card card-commercial">
    <div class="card-art" role="img" aria-label="Line illustration of business people connected around a globe"></div>
    <h3>Commercial<br>Mediation</h3>
    <p>Praesent sit amet est In dictum dolor eu dictum porttitor enim felis</p>
  </div>
  <div class="card card-family">
    <div class="card-art" role="img" aria-label="Line illustration of a family inside a heart"></div>
    <h3>Family<br>Mediation</h3>
    <p>Praesent sit amet est In dictum dolor eu dictum porttitor enim felis</p>
  </div>
  <div class="card card-nonprofit">
    <div class="card-art" role="img" aria-label="Line illustration of hands holding a group of people"></div>
    <h3>Nonprofits<br>Mediation</h3>
    <p>Praesent sit amet est In dictum dolor eu dictum porttitor enim felis</p>
  </div>
</section>

<div class="abs intro-photo" role="img" aria-label="An older woman resting her head in her hand on a sofa while her partner sits in the background"></div>
<h2 class="abs section-title intro-title">Have you finally<br>had enough?</h2>
<div class="abs rule intro-rule"></div>
<div class="abs intro-text">
  <p>Is there a conflict causing undue stress in your life? Have you and your partner, team or family members reached the tipping point where you need help finding a resolution? It’s okay. Harborline Mediation Group (HMG) will help you find the path to a peaceful, satisfying and mutually determined, positive path forward.</p>
  <p>First, know that being in conflict is common in most people’s lives. You and those you are struggling with are far from alone as disputes exist everywhere. When two or more parties feel they aren’t getting anywhere in their discussions and reach an impasse, professional mediation is often the best solution. It saves time, reduces legal costs and can rescue precious relationships.</p>
</div>

<div class="abs peace-band" role="img" aria-label="A family sitting together outdoors in warm evening light"></div>
<div class="abs peace-shade"></div>
<h2 class="abs peace-title">Peace is priceless</h2>
<div class="abs peace-rule"></div>
<div class="abs peace-text">
  <p>Mediation is a subtle yet organized approach to addressing conflict. It starts with building a platform from which mutually satisfying solutions may evolve. This platform evolves by jointly exploring important factors and desires and clarifying mis-understandings between those who have a stake in the conflict.</p>
  <p>The mediation process is focused on discerning parties’ interests, which are often camouflaged behind assertions and unspoken needs as well as clouded by material demands. Once revealed, clarified and understood, parties can better understand and appreciate each other, and agree to collaborate on how to move forward on resolutions that in many cases benefit everyone involved. Even if a resolution is not achieved, each party more clearly understands the other’s perspective and reasoning.</p>
</div>
<a class="abs btn-solid">CONTACT US TO LEARN MORE</a>

<h2 class="abs section-title services-title">Traditional and virtual<br>mediation services</h2>
<div class="abs rule services-rule"></div>
<p class="abs services-text">Clients have the option of meeting in person when it suits them or remotely using videoconferencing tools like MeetSpace, LinkRoom and TalkHub. Online meetings are becoming the norm for many and we are happy to accommodate our clients’ venue preferences whether digital or face to face in a safe setting. In person meetings can be held in our office, a workplace, or even in a family’s living room.</p>
<div class="abs services-photo" role="img" aria-label="An older couple arguing on a blue sofa, the man holding his head in frustration"></div>

<div class="abs consult-band" role="img" aria-label="People meeting at a table, tinted in teal and green"></div>
<h2 class="abs consult-title">Free 30-minute consultation</h2>
<div class="abs consult-rule"></div>
<p class="abs consult-text">Are you and another party struggling with a conflict? HMG offers 30 minutes of initial consultation free by telephone or video conference.</p>
<a class="abs btn-outline">SCHEDULE YOUR CONSULTATION</a>

<footer>
  <div class="abs footer-brand"><span class="footer-dot"></span>Harborline Mediation Group</div>
  <nav class="abs footer-nav">
    <span>Home</span><span>Mediation Services</span><span>Conflict Consulting</span><span>Negotiation</span><span>About Us</span><span>Blog</span><span>Contact</span>
  </nav>
  <p class="abs copyright">© 2020 Company Name | All Rights Reserved</p>
  <div class="abs social"><span></span><span></span><span></span><span></span></div>
</footer>

</body>
</html>
```